Business card design needed for elearning/LMS consultant

I'm an elearning and learning management system (LMS) consultant that requires a minimalist, technology/cutting edge, business card. I do not have a logo or colour scheme. I offer clients hands on expertise in 'elearning authouring', 'LMS ecosystems', 'elearning strategy', 'technical implementation', 'mlearning', 'LMS evaluation', 'big data', 'learner analytics' and 'reporting strategy', 'social learning', 'elearning blueprint'. I'm thinking a 'tag cloud' of the above services on the back of the card, with contact details on front, but unsure if it's passe so please don't let it constrain you.

Target Market(s)

C-level executives, learning and development senior management,

Industry/Entity Type

Business

Contact Information for Business Card

Dorian Vastwick
dorian.vastwick@mailbrook.net
0417 362 958

Requirements
Should not have
• cheesy headshots, overused stockphotos, CLIPART and comic sans ;)

```html
<!DOCTYPE html>
<html lang="en">
<head>
<meta charset="utf-8">
<title>Dorian Vastwick – Business Card</title>
<link rel="stylesheet" href="https://fonts.googleapis.com/css2?family=Comfortaa:wght@300;400&family=Delius&display=swap">
<style>
  :root {
    --page-bg: #1c1c1e;
    --card-navy: #27304c;
    --card-navy-deep: #1f2740;
    --ink-bright: #f2f3f5;
    --ink-soft: #c9ccd3;
    --ink-muted: #a9adb8;
    --accent-lime: #b9c62a;
  }
  * { margin: 0; padding: 0; box-sizing: border-box; }
  html, body {
    width: 1200px; height: 900px; overflow: hidden;
    background: var(--page-bg);
  }
  .stage {
    position: relative; width: 1200px; height: 900px;
    display: flex; flex-direction: column; align-items: center; justify-content: center; gap: 40px;
  }
  .card {
    position: relative; width: 700px; height: 400px;
    background: linear-gradient(160deg, var(--card-navy) 0%, var(--card-navy-deep) 100%);
    box-shadow: 0 10px 30px rgba(0,0,0,.5);
    overflow: hidden;
  }
  /* Contact side */
  .contact {
    position: absolute; left: 0; right: 0; top: 120px;
    text-align: center; font-family: "Comfortaa", sans-serif;
  }
  .contact__name {
    font-size: 34px; font-weight: 300; color: var(--ink-soft); letter-spacing: .5px;
    margin-bottom: 34px;
  }
  .contact__email { font-size: 18px; color: var(--accent-lime); margin-bottom: 12px; }
  .contact__phone { font-size: 22px; font-weight: 300; color: var(--ink-muted); letter-spacing: 1px; }

  /* Services tag cloud side */
  .tag {
    position: absolute; white-space: nowrap; line-height: 1;
    font-family: "Delius", sans-serif; color: var(--ink-muted);
  }
  .tag--major { color: var(--ink-bright); font-weight: 700; }
  .tag--vertical { writing-mode: vertical-rl; transform: rotate(180deg); }
</style>
</head>
<body>
<main class="stage">
  <section class="card card--contact" aria-label="Contact side">
    <div class="contact">
      <p class="contact__name">Dorian Vastwick</p>
      <p class="contact__email">dorian.vastwick@mailbrook.net</p>
      <p class="contact__phone">0417 362 958</p>
    </div>
  </section>

  <section class="card card--services" aria-label="Services side">
    <span class="tag tag--vertical" style="left:138px; top:78px; font-size:11px;">mlearning</span>
    <span class="tag" style="left:162px; top:70px; font-size:19px;">reporting strategy</span>
    <span class="tag" style="left:372px; top:66px; font-size:11px;">big data</span>
    <span class="tag" style="left:196px; top:104px; font-size:19px;">LMS technical implementation</span>
    <span class="tag tag--major" style="left:128px; top:134px; font-size:32px;">LMS evaluation and selection</span>
    <span class="tag" style="left:400px; top:180px; font-size:11px;">LMS project management</span>
    <span class="tag tag--major" style="left:22px; top:200px; font-size:33px;">e-learning strategy</span>
    <span class="tag tag--vertical" style="left:338px; top:186px; font-size:30px; color:var(--ink-soft);">mobile learning</span>
    <span class="tag tag--major" style="left:382px; top:200px; font-size:32px; color:var(--ink-soft);">learner analytics</span>
    <span class="tag tag--vertical" style="left:394px; top:244px; font-size:10px;">e-learning blueprint</span>
    <span class="tag" style="left:430px; top:252px; font-size:20px;">social learning</span>
    <span class="tag" style="left:120px; top:256px; font-size:20px;">e-learning authoring</span>
    <span class="tag" style="left:210px; top:290px; font-size:12px;">LMS ecosystem</span>
  </section>
</main>
</body>
</html>
```